Bench Advertisement - We Buy Houses Design Needed

Need a catchy, simple but elegant design for bus benches to advertise our company.

We need our website, or phone number, and a smal description (1-2 bulletpoints of what we do and what we offer)

The tricky part is for the designer to fit everything and make the website name as part of the title and fitting everything so that people passing by on the street can see what we offer.

Our website is quickhomebuyerdesk.com - (916) 482-3091

Something simple but something that catches the eye of walking pedestrians, and drivers driving by the bench.

Our company buys houses, any condition, any situation, we buy houses for cash and close quickly. You can use this description to create a few bulletpoints however you like. Must follow dimensions in attachment.

Target Market(s)

People in foreclosure, about to lose their homes, people that need a quick cash sale of their property

Industry/Entity Type

Real Estate

Requirements
Must have
• catchy, website name, phone number, few brief bulletpoints about what we offer, colors that will catch peoples eye while walking or driving - advertisement will be placed on bus benches - visit our website to see the type of houses we buy - Also have more work for winner of design with possible bonuses
Nice to have
• Feel free to use description or images on our website - make sure the description is just bullet points and it fits with the overall theme / size of the advertisement - Bold bright colors - put yourself in their shoes (if you were going through financial difficulties and about to lose your house to foreclosure or auction, what would you want to see to pick up the phone and call us for a quick sale of your house?) (or if you have a house that you are having a problem with, problem renters, unkept/beat up house, what would make you want to call us and sell your house to us?)

```html
<!DOCTYPE html>
<html lang="en">
<head>
<meta charset="utf-8">
<title>Quick Home Buyer Desk – Bench Advertisement</title>
<link rel="stylesheet" href="https://fonts.googleapis.com/css2?family=Libre+Franklin:wght@600;800;900&display=swap">
<style>
  :root {
    --page: #ffffff;
    --orange: #e88b3e;
    --ink: #000000;
    --white: #ffffff;
  }
  html, body {
    margin: 0;
    padding: 0;
    width: 1200px;
    height: 1200px;
    overflow: hidden;
    background: var(--page);
  }
  .canvas {
    position: relative;
    width: 1200px;
    height: 1200px;
    background: var(--page);
  }
  .bench-ad {
    position: absolute;
    left: 110px;
    top: 128px;
    width: 994px;
    height: 284px;
    background: var(--orange);
    overflow: hidden;
    font-family: "Libre Franklin", Arial, sans-serif;
  }
  .headline-word {
    position: absolute;
    left: 22px;
    top: -88px;
    margin: 0;
    font-size: 300px;
    font-weight: 900;
    line-height: 1;
    letter-spacing: -14px;
    background: linear-gradient(to bottom, var(--ink) 0%, var(--ink) 58%, var(--orange) 84%);
    -webkit-background-clip: text;
    background-clip: text;
    color: transparent;
  }
  .domain {
    position: absolute;
    left: 26px;
    top: 148px;
    margin: 0;
    font-size: 80px;
    font-weight: 800;
    line-height: 1;
    letter-spacing: -2px;
    color: var(--white);
  }
  .tagline {
    position: absolute;
    left: 28px;
    top: 236px;
    margin: 0;
    font-size: 28px;
    font-weight: 800;
    line-height: 1;
    color: var(--ink);
    white-space: nowrap;
  }
  .tagline .emphasis {
    text-decoration: underline;
    text-decoration-thickness: 2px;
    text-underline-offset: 5px;
  }
  .brand {
    position: absolute;
    left: 716px;
    top: 136px;
    display: flex;
    align-items: center;
    gap: 8px;
  }
  .brand-square {
    width: 18px;
    height: 18px;
    background: var(--ink);
  }
  .brand-name {
    font-size: 17px;
    font-weight: 600;
    color: var(--ink);
    white-space: nowrap;
  }
</style>
</head>
<body>
  <main class="canvas">
    <section class="bench-ad" aria-label="Bench advertisement">
      <h1 class="headline-word">Quick</h1>
      <p class="domain">homebuyerdesk.com</p>
      <div class="brand">
        <span class="brand-square"></span>
        <span class="brand-name">QUICK HOME BUYER DESK</span>
      </div>
      <p class="tagline">Call or Text Us Now for a <span class="emphasis">No Obligation</span> Offer (916) 482-3091</p>
    </section>
  </main>
</body>
</html>
```